Property Management Company Business Cards

Need business cards for a property management company located in Michigan. We manage houses for clients all over the world. Young and modern company, looking for eye catching design. Please work with the attached logo.

Industry/Entity Type

Property Management

Requirements
Must have
• Need lines for address, telephone number, fax number, web site.

Also lines for name, and job title

```html
<!DOCTYPE html>
<html lang="en">
<head>
<meta charset="utf-8">
<title>Lakeshore Harbor Management – Business Cards</title>
<link rel="stylesheet" href="https://fonts.googleapis.com/css2?family=Open+Sans:wght@400;600;700&display=swap">
<style>
  :root {
    --backdrop: #2b2219;
    --card-dark: #0d0d0d;
    --card-dark-tone: #151515;
    --card-border: #f2f2f2;
    --brand-blue: #27a4de;
    --brand-grey: #d9d9d9;
    --ink-dark: #2c3a45;
    --watermark: #2f5f78;
    --contact-text: #f4f8fb;
  }
  * { box-sizing: border-box; margin: 0; padding: 0; }
  html, body {
    width: 1200px;
    height: 887px;
    overflow: hidden;
    background: var(--backdrop);
    font-family: "Open Sans", Arial, sans-serif;
  }
  .canvas {
    position: relative;
    width: 1200px;
    height: 887px;
  }
  .card {
    position: absolute;
    width: 419px;
    height: 682px;
    border-radius: 18px;
    overflow: hidden;
  }

  /* Front card */
  .card-front {
    left: 120px;
    top: 104px;
    background: var(--card-dark);
    border: 3px solid var(--card-border);
  }
  .front-pattern-area {
    position: absolute;
    inset: 0;
    background: var(--card-dark-tone);
  }
  .front-mark {
    position: absolute;
    left: 50%;
    top: 250px;
    width: 96px;
    height: 96px;
    margin-left: -48px;
    border-radius: 50%;
    background: var(--brand-blue);
  }
  .front-name {
    position: absolute;
    left: 0;
    right: 0;
    top: 570px;
    text-align: center;
    color: var(--brand-grey);
    font-weight: 600;
  }
  .front-name .line-main {
    display: block;
    font-size: 34px;
    line-height: 40px;
    letter-spacing: 0.5px;
  }
  .front-name .line-sub {
    display: block;
    font-size: 24px;
    line-height: 32px;
    letter-spacing: 8px;
  }

  /* Back card */
  .card-back {
    left: 664px;
    top: 101px;
    background: var(--brand-blue);
    border: 3px solid var(--card-border);
  }
  .back-watermark {
    position: absolute;
    left: 150px;
    top: 440px;
    width: 250px;
    height: 250px;
    border-radius: 50%;
    background: var(--watermark);
    opacity: 0.75;
  }
  .back-header {
    position: absolute;
    left: 22px;
    top: 30px;
    display: flex;
    align-items: center;
    gap: 14px;
  }
  .back-header .header-dot {
    width: 48px;
    height: 48px;
    border-radius: 50%;
    background: var(--ink-dark);
  }
  .back-header .header-rule {
    width: 2px;
    height: 66px;
    background: var(--ink-dark);
  }
  .back-header .header-name {
    color: var(--ink-dark);
    font-weight: 700;
  }
  .header-name .line-main {
    display: block;
    font-size: 25px;
    line-height: 30px;
  }
  .header-name .line-sub {
    display: block;
    font-size: 17px;
    line-height: 22px;
    letter-spacing: 6.5px;
  }
  .holder {
    position: absolute;
    left: 106px;
    top: 118px;
    color: var(--contact-text);
  }
  .holder-name {
    display: block;
    font-size: 24px;
    line-height: 30px;
    font-weight: 700;
  }
  .holder-title {
    display: block;
    font-size: 17px;
    line-height: 24px;
    font-weight: 400;
    color: var(--ink-dark);
  }
  .contact-list {
    position: absolute;
    left: 28px;
    top: 213px;
    list-style: none;
  }
  .contact-item {
    display: flex;
    align-items: center;
    height: 40px;
    margin-bottom: 20px;
    color: var(--contact-text);
    font-size: 25px;
    font-weight: 400;
  }
  .contact-icon {
    width: 40px;
    height: 40px;
    margin-right: 38px;
    flex: none;
  }
  .contact-icon * {
    fill: none;
    stroke: var(--ink-dark);
    stroke-width: 3;
    stroke-linejoin: round;
    stroke-linecap: round;
  }
  .contact-icon .solid { fill: var(--ink-dark); stroke: none; }
</style>
</head>
<body>
<main class="canvas">

  <section class="card card-front" aria-label="Business card front">
    <div class="front-pattern-area" role="img" aria-label="Dark repeating brand pattern background"></div>
    <div class="front-mark"></div>
    <h1 class="front-name">
      <span class="line-main">LAKESHORE HARBOR</span>
      <span class="line-sub">MANAGEMENT</span>
    </h1>
  </section>

  <section class="card card-back" aria-label="Business card back">
    <div class="back-watermark"></div>

    <header class="back-header">
      <div class="header-dot"></div>
      <div class="header-rule"></div>
      <h2 class="header-name">
        <span class="line-main">LAKESHORE HARBOR</span>
        <span class="line-sub">MANAGEMENT</span>
      </h2>
    </header>

    <p class="holder">
      <span class="holder-name">Name</span>
      <span class="holder-title">Job Title</span>
    </p>

    <ul class="contact-list">
      <li class="contact-item">
        <svg class="contact-icon" viewBox="0 0 40 40" aria-hidden="true">
          <path d="M4 20 L20 5 L36 20"/>
          <path d="M9 16 V35 H31 V16"/>
          <path d="M17 35 V25 H23 V35"/>
        </svg>
        <span>Address</span>
      </li>
      <li class="contact-item">
        <svg class="contact-icon" viewBox="0 0 40 40" aria-hidden="true">
          <rect x="12" y="8" width="16" height="28" rx="3"/>
          <path d="M16 8 V3"/>
          <rect class="solid" x="16" y="13" width="8" height="7"/>
        </svg>
        <span>Telephone</span>
      </li>
      <li class="contact-item">
        <svg class="contact-icon" viewBox="0 0 40 40" aria-hidden="true">
          <rect x="11" y="4" width="18" height="10"/>
          <rect x="5" y="14" width="30" height="13" rx="2"/>
          <rect x="11" y="23" width="18" height="13"/>
          <path d="M15 28 H25 M15 32 H25"/>
        </svg>
        <span>Fax</span>
      </li>
      <li class="contact-item">
        <svg class="contact-icon" viewBox="0 0 40 40" aria-hidden="true">
          <circle cx="19" cy="19" r="15"/>
          <ellipse cx="19" cy="19" rx="6" ry="15"/>
          <path d="M4 19 H34 M7 11 H31 M7 27 H31"/>
        </svg>
        <span>Website</span>
      </li>
    </ul>
  </section>

</main>
</body>
</html>
```